letter head for a construction company

Company Name: Zaviro Construction Limited

Address: Kilele Street, Tengeru Shores, Dar es salaam, Tanzania

Phone: 0754382916

email : info@zaviroconstruction.example

website : www.zaviroconstruction.example

```html
<!DOCTYPE html>
<html lang="en">
<head>
<meta charset="utf-8">
<title>Zaviro Construction Limited – Letterhead</title>
<link href="https://fonts.googleapis.com/css2?family=Arimo:wght@400&family=Montserrat:wght@600&family=Mulish:wght@700;800&display=swap" rel="stylesheet">
<style>
  :root {
    --backdrop: #e2e2e2;
    --paper: #ffffff;
    --ink-dark: #464646;
    --ink-body: #555555;
    --ink-soft: #7a7a7a;
    --rule: #bdbdbd;
    --accent: #ee7d11;
    --tint-grey: #ececec;
    --tint-orange: #fdf0e4;
  }
  * { box-sizing: border-box; margin: 0; padding: 0; }
  html, body { width: 978px; height: 1200px; overflow: hidden; background: var(--backdrop); }
  .letterhead {
    position: absolute; left: 79px; top: 20px;
    width: 820px; height: 1160px;
    background: var(--paper);
    overflow: hidden;
  }
  .brand {
    position: absolute; left: 0; right: 0; top: 72px;
    display: flex; justify-content: center; align-items: center; gap: 10px;
    font-family: "Montserrat", sans-serif; font-weight: 600;
    font-size: 19px; letter-spacing: 2.5px; color: var(--ink-dark);
  }
  .brand-mark { width: 14px; height: 14px; background: var(--accent); }
  .greeting {
    position: absolute; left: 75px; top: 356px;
    font-family: "Mulish", sans-serif; font-weight: 800;
    font-size: 19px; color: var(--ink-dark);
  }
  .letter-body {
    position: absolute; left: 73px; top: 412px; width: 672px;
    font-family: "Arimo", sans-serif; font-size: 13.8px; line-height: 16.8px;
    color: var(--ink-body);
  }
  .letter-body p + p { margin-top: 14.5px; }
  .closing {
    position: absolute; left: 75px; top: 758px;
    font-family: "Mulish", sans-serif; font-weight: 700; font-size: 11px;
    color: var(--ink-dark);
  }
  .signature {
    position: absolute; left: 75px; top: 808px; width: 135px; height: 38px;
    background: linear-gradient(90deg, #ededed, #f6f6f6);
    border-radius: 3px;
  }
  .backdrop-shape {
    position: absolute; left: -150px; top: 880px; width: 390px; height: 390px;
    border-radius: 50%; background: var(--tint-grey); opacity: .7;
  }
  .footer {
    position: absolute; left: 252px; width: 517px; top: 1080px;
    font-family: "Arimo", sans-serif; color: var(--ink-soft);
  }
  .footer-address { text-align: center; font-size: 12.5px; line-height: 18px; }
  .footer-rule { height: 1px; background: var(--rule); margin: 4px 0 6px; }
  .footer-contacts {
    display: flex; justify-content: space-between; align-items: center;
    font-size: 12.5px; white-space: nowrap;
  }
  .contact { display: flex; align-items: center; gap: 6px; }
  .contact svg { width: 10px; height: 10px; flex: none; }
</style>
</head>
<body>
  <main class="letterhead">
    <div class="backdrop-shape"></div>

    <header class="brand">
      <span class="brand-mark"></span>
      <span class="brand-name">ZAVIRO CONSTRUCTION LIMITED</span>
    </header>

    <h1 class="greeting">Dear Mr. Mwakasege,</h1>

    <section class="letter-body">
      <p>Lorem ipsum dolor sit amet, consectetuer adipiscing elit, sed diam nonmmy nibh euismod tincidunt ut laor eet dolore magna aliquam erat volutpat. Ut wisi enim ad minim veniam, quis nostrud exerci tationmcorper suscipit lobortis nisl ut aliquip ex ea commodo consequat. Duis autem vel eum iriure dolor in hendrerit in vulputate velit esse molestie consequat, vel illum dolore eu feugiat</p>
      <p>Rorem ipsum dolor sit amet, consectetuer adipiscing elit, sed diam nonmmy nibh euismod tincidunt ut laor eet dolore magna aliquam erat volutpat. Ut wisi enim ad minim veniam, quis nostrud exerci tationmcorper suscipit lobortis nisl ut aliquip ex ea commodo consequat. Duis autem vel eum iriure dolor in hendrerit in vulputate velit esse molest</p>
      <p>Dorem ipsum dolor sit amet, consectetuer adipiscing elit, sed diam nonmmy nibh euismod tincidunt ut laor eet dolore magna aliquam erat volutpat. Ut wisi enim ad minim veniam, quis nostrud exerci tationmcorper suscipit lobortis nisl ut aliquip ex ea commodo consequat. Duis autem vel eum iriure dolor in hendrerit in suscipit lobortis nisl ut aliquip ex ea commodo consequat. Duis autem vel eum iriure dolor in hendrerit in vulputate velit esse molestie consequat, vel illum</p>
      <p>Sorem ipsum dolor sit amet, consectetuer adipiscing elit, sed diam nonmmy nibh euismod tincidunt ut laor eet dolore magna aliquam erat volutpat. Ut wisi enim ad minim veniam, quis nostrud exerci tationmcorper suscipit lobortis nisl ut aliquip ex ea commodo consequat. Duis autem vel eum iriure dolor in</p>
    </section>

    <p class="closing">Sincerely,</p>
    <div class="signature" role="img" aria-label="Handwritten signature of the sender"></div>

    <footer class="footer">
      <p class="footer-address">Kilele Street, Tengeru Shores, Dar es salaam, Tanzania</p>
      <div class="footer-rule"></div>
      <div class="footer-contacts">
        <span class="contact">
          <svg viewBox="0 0 10 10" aria-hidden="true"><path d="M2 0.8 L3.6 2.8 L2.7 3.9 Q3.8 6 6.1 7.3 L7.2 6.4 L9.2 8 L8 9.4 Q3.5 9 0.6 2.2 Z" fill="var(--accent)"/></svg>
          0754382916
        </span>
        <span class="contact">
          <svg viewBox="0 0 10 10" aria-hidden="true"><rect x="0.5" y="2" width="9" height="6" fill="var(--accent)"/><path d="M0.5 2 L5 5.6 L9.5 2" fill="none" stroke="#fff" stroke-width="0.9"/></svg>
          info@zaviroconstruction.example
        </span>
        <span class="contact">
          <svg viewBox="0 0 10 10" aria-hidden="true"><circle cx="5" cy="5" r="4.5" fill="var(--accent)"/><path d="M0.5 5 H9.5 M5 0.5 Q2.5 5 5 9.5 M5 0.5 Q7.5 5 5 9.5" fill="none" stroke="#fff" stroke-width="0.8"/></svg>
          www.zaviroconstruction.example
        </span>
      </div>
    </footer>
  </main>
</body>
</html>
```